KTR Business Cards

We require business cards for our business. We would like a matte black back to the card, with our logo centred in the middle. The front side of the card is open to design.

Target Market(s)

Clients looking for legal services (professional)

Industry/Entity Type

Legal

Contact Information for Business Card

Dario Velkenor
Partner
Mobile: 0471 386 524
Email: dario@ktrlaw.co
Website: www.ktrlaw.co
Level 3, 118 Pembury Street
Sydney NSW 2000

Font styles to use
Other font styles liked:
• Avenir

Colors
f04a50
ffffff
1b1b1b

Requirements
Must have
• Black back with logo included in the centre of the card.
• Our font is Avenir.

```html
<!DOCTYPE html>
<html lang="en">
<head>
<meta charset="utf-8">
<title>KTR Legal — Business Cards</title>
<link rel="stylesheet" href="https://fonts.googleapis.com/css2?family=Nunito+Sans:wght@400;600;700;800&display=swap">
<style>
  :root {
    --backdrop: #e4e4e6;
    --card-white: #ffffff;
    --card-black: #0c0c0c;
    --ink: #1b1b1b;
    --ink-soft: #3a3a3a;
    --accent: #c8214b;
    --paper-white: #ffffff;
  }
  * { box-sizing: border-box; margin: 0; padding: 0; }
  html, body {
    width: 1200px;
    height: 800px;
    overflow: hidden;
    background: var(--backdrop);
    font-family: "Nunito Sans", "Avenir", sans-serif;
  }
  .sheet {
    position: relative;
    width: 1200px;
    height: 800px;
    display: flex;
    align-items: center;
    justify-content: center;
    gap: 60px;
  }
  .card {
    position: relative;
    width: 525px;
    height: 300px;
    border-radius: 3px;
    box-shadow: 0 10px 28px rgba(0,0,0,0.16), 0 2px 6px rgba(0,0,0,0.10);
    overflow: hidden;
  }

  /* Front */
  .card--front { background: var(--card-white); color: var(--ink); }
  .brand {
    position: absolute;
    display: flex;
    align-items: center;
    gap: 12px;
  }
  .brand__square {
    width: 26px;
    height: 26px;
    background: var(--accent);
  }
  .brand__name {
    font-weight: 800;
    letter-spacing: 0.06em;
    line-height: 1;
  }
  .card--front .brand { top: 36px; left: 40px; }
  .card--front .brand__name { font-size: 34px; color: var(--ink); }

  .contact {
    position: absolute;
    left: 40px;
    top: 118px;
    font-size: 14px;
    line-height: 1.45;
    color: var(--ink-soft);
  }
  .contact__address { margin-bottom: 8px; }
  .contact__list { list-style: none; }
  .contact__item {
    display: flex;
    align-items: center;
    gap: 8px;
  }
  .contact__icon { width: 12px; height: 12px; flex: none; }

  .person {
    position: absolute;
    right: 40px;
    bottom: 44px;
    text-align: right;
  }
  .person__name {
    font-size: 21px;
    font-weight: 600;
    color: var(--accent);
    letter-spacing: 0.01em;
  }
  .person__role {
    font-size: 14px;
    color: var(--ink-soft);
    margin-top: 2px;
  }

  /* Back */
  .card--back {
    background: var(--card-black);
    display: flex;
    align-items: center;
    justify-content: center;
  }
  .card--back .brand { position: static; gap: 16px; }
  .card--back .brand__square { width: 38px; height: 38px; }
  .card--back .brand__name { font-size: 52px; color: var(--paper-white); }
</style>
</head>
<body>
<main class="sheet">

  <section class="card card--front" aria-label="Business card front">
    <div class="brand">
      <span class="brand__square"></span>
      <span class="brand__name">KTR</span>
    </div>

    <div class="contact">
      <p class="contact__address">Level 3, 118 Pembury Street<br>Sydney NSW 2000</p>
      <ul class="contact__list">
        <li class="contact__item">
          <svg class="contact__icon" viewBox="0 0 12 12" aria-hidden="true">
            <rect x="2.5" y="0.75" width="7" height="10.5" rx="1.2" fill="none" stroke="var(--accent)" stroke-width="1.3"/>
            <line x1="5" y1="9.2" x2="7" y2="9.2" stroke="var(--accent)" stroke-width="1.2"/>
          </svg>
          <span>0471 386 524</span>
        </li>
        <li class="contact__item">
          <svg class="contact__icon" viewBox="0 0 12 12" aria-hidden="true">
            <rect x="0.75" y="2" width="10.5" height="8" fill="none" stroke="var(--accent)" stroke-width="1.3"/>
            <polyline points="0.9,2.4 6,6.6 11.1,2.4" fill="none" stroke="var(--accent)" stroke-width="1.3"/>
          </svg>
          <span>dario@ktrlaw.co</span>
        </li>
        <li class="contact__item">
          <svg class="contact__icon" viewBox="0 0 12 12" aria-hidden="true">
            <circle cx="6" cy="6" r="5.2" fill="none" stroke="var(--accent)" stroke-width="1.2"/>
            <ellipse cx="6" cy="6" rx="2.3" ry="5.2" fill="none" stroke="var(--accent)" stroke-width="1"/>
            <line x1="0.8" y1="6" x2="11.2" y2="6" stroke="var(--accent)" stroke-width="1"/>
          </svg>
          <span>www.ktrlaw.co</span>
        </li>
      </ul>
    </div>

    <div class="person">
      <p class="person__name">Dario Velkenor</p>
      <p class="person__role">Partner</p>
    </div>
  </section>

  <section class="card card--back" aria-label="Business card back">
    <div class="brand">
      <span class="brand__square"></span>
      <span class="brand__name">KTR</span>
    </div>
  </section>

</main>
</body>
</html>
```